Fiscal Sponsorship Program Flyer

We are seeking a designer to create a 1-2 flyer that explains our fiscal sponsorship program. This flyer will be used to recruit new projects that might be interested in utilizing our fiscal sponsorship services. The pertinent information about our program can be found in the attached PDF. For users who cannot access the PDF, please try this link: https://files.brivanto.net/slides/d/7QtR2wXkLmZp9HvCs4YdNe8JfGaUoBi3Tx5Wl0KyRc2s/view?mode=shared

Target Market(s)

New charitable projects that do not yet have their own 501(c)(3) status, and are seeking a fiscal sponsor.

Industry/Entity Type

Nonprofit/Charity

Requirements
Must have
• The flyer must include the language and detail included on the attached PDF. The desire is to reformat this to be more appealing and easy to read.

```html
<!DOCTYPE html>
<html lang="en">
<head>
<meta charset="utf-8">
<title>Meridian Foundation – Fiscal Sponsorship Program Flyer</title>
<link rel="stylesheet" href="https://fonts.googleapis.com/css2?family=DM+Serif+Display&family=Montserrat:ital,wght@0,300;0,400;0,700;0,800;0,900;1,300;1,800&family=Open+Sans:wght@400;600;700&display=swap">
<style>
  :root {
    --stage: #262626;
    --ink: #1b1b1b;
    --white: #ffffff;
    --navy: #0b2f66;
    --navy-deep: #082554;
    --blue: #0a7ff0;
    --blue-mid: #0a5fc6;
    --blue-dark: #0a3e84;
    --accent: #0a84ff;
    --heading-navy: #0b2a5c;
    --sky-dusk: #5a7a95;
  }
  * { box-sizing: border-box; margin: 0; padding: 0; }
  html, body { width: 1200px; height: 840px; overflow: hidden; background: var(--stage); }
  body { position: relative; font-family: "Open Sans", sans-serif; color: var(--ink); }

  .page { position: absolute; top: 20px; width: 566px; height: 799px; background: var(--white); overflow: hidden; }
  .page--intro { left: 23px; }
  .page--details { left: 611px; }

  /* ---------- Intro page ---------- */
  .hero { position: absolute; left: 0; top: 0; width: 566px; height: 361px;
    background: radial-gradient(ellipse at 52% 42%, #8fa9bc 0%, var(--sky-dusk) 22%, #24384a 55%, #121a22 100%); }
  .hero__title { position: absolute; left: 0; right: 0; top: 94px; text-align: center;
    font-family: "DM Serif Display", serif; font-size: 42px; color: var(--white); line-height: 1; }
  .hero__subtitle { position: absolute; right: 84px; top: 139px; font-family: "Montserrat", sans-serif;
    font-weight: 300; font-size: 15px; color: var(--white); }
  .hero__intro { position: absolute; left: 30px; right: 30px; top: 260px; text-align: center;
    font-family: "Montserrat", sans-serif; font-weight: 300; font-size: 12.6px; line-height: 1.22; color: var(--white); }
  .hero__intro strong { font-weight: 800; font-style: italic; }
  .hero__notch { position: absolute; left: 0; top: 352px; width: 566px; height: 30px; }

  .definition { position: absolute; left: 0; top: 377px; width: 300px; height: 126px;
    background: linear-gradient(90deg, var(--navy-deep), var(--blue-dark) 40%, var(--blue));
    color: var(--white); font-size: 10.6px; line-height: 1.24; text-align: center; padding: 20px 14px 0 18px; }
  .definition__bevel { position: absolute; left: 300px; top: 377px; width: 19px; height: 126px; }
  .definition__heading { position: absolute; left: 319px; top: 386px; width: 247px; height: 109px;
    background: linear-gradient(90deg, var(--blue-mid), var(--blue));
    font-family: "Montserrat", sans-serif; font-weight: 900; font-size: 28px; line-height: 0.9;
    color: var(--white); padding: 19px 0 0 11px; }

  .eligibility { position: absolute; left: 18px; right: 18px; top: 522px; text-align: center; }
  .eligibility__question { font-family: "Montserrat", sans-serif; font-weight: 800; font-style: italic;
    font-size: 11px; color: var(--accent); margin-bottom: 4px; }
  .eligibility__answer { font-family: "Montserrat", sans-serif; font-weight: 700; font-size: 10.2px; line-height: 1.22; }

  .philosophy__heading { position: absolute; left: 0; top: 616px; width: 249px; height: 136px;
    background: linear-gradient(90deg, var(--blue), var(--blue-mid));
    font-family: "Montserrat", sans-serif; font-weight: 900; font-size: 28px; line-height: 0.9;
    color: var(--white); text-align: right; padding: 19px 12px 0 0; }
  .philosophy__bevel { position: absolute; left: 249px; top: 616px; width: 18px; height: 136px; }
  .philosophy__text { position: absolute; left: 266px; top: 605px; width: 300px; height: 158px;
    background: linear-gradient(90deg, var(--blue-mid), var(--navy-deep));
    color: var(--white); font-size: 11.2px; line-height: 1.2; text-align: center; padding: 14px 14px 0; }
  .philosophy__text p + p { margin-top: 12px; }

  /* ---------- Details page ---------- */
  .values__band { position: absolute; left: 0; top: 0; width: 566px; height: 76px;
    background: linear-gradient(90deg, var(--blue-mid), var(--blue)); color: var(--white);
    font-family: "Montserrat", sans-serif; font-weight: 900; font-size: 30px; letter-spacing: 0.5px;
    text-align: center; padding-top: 19px; }
  .values__list { position: absolute; left: 0; top: 76px; width: 566px; height: 207px;
    background: linear-gradient(90deg, #fafafa, #e6e6e6); padding: 14px 40px 0 44px;
    font-size: 11.3px; line-height: 1.36; list-style: none; text-align: justify; }
  .values__list li + li { margin-top: 14px; }
  .value__name { font-family: "Montserrat", sans-serif; font-weight: 800; color: var(--accent); font-size: 12.2px; }

  .commitments__band { position: absolute; left: 0; top: 283px; width: 566px; height: 36px;
    background: linear-gradient(90deg, var(--blue-mid), var(--blue)); color: var(--white);
    font-family: "Montserrat", sans-serif; font-weight: 300; font-style: italic; font-size: 21px;
    text-align: center; padding-top: 4px; }
  .commitments__list { position: absolute; left: 0; top: 319px; width: 566px; height: 209px;
    background: linear-gradient(90deg, #fafafa, #e8e8e8); list-style: none; padding: 10px 39px 0 72px;
    font-size: 10.1px; line-height: 1.3; }
  .commitments__list li { position: relative; margin-bottom: 13px; }
  .commitments__list svg { position: absolute; left: -23px; top: -1px; width: 16px; height: 13px; }

  .fees__title { position: absolute; left: 0; right: 0; top: 528px; height: 32px; line-height: 32px; text-align: center;
    font-family: "Montserrat", sans-serif; font-weight: 800; font-size: 19px; color: var(--heading-navy); }
  .fee-tier { position: absolute; top: 560px; width: 189px; height: 239px; color: var(--white);
    padding: 18px 0 0 16px; font-size: 9.6px; line-height: 1.68; }
  .fee-tier--basic { left: 0; background: var(--blue); }
  .fee-tier--standard { left: 189px; background: var(--blue-mid); border-left: 1px solid rgba(255,255,255,0.5); }
  .fee-tier--premium { left: 378px; background: var(--blue-dark); padding-left: 14px; }
  .fee-tier__name { font-family: "Montserrat", sans-serif; font-weight: 700; font-size: 13.5px; white-space: nowrap;
    margin: 0 0 10px 18px; line-height: 1.3; }
  .fee-tier--standard .fee-tier__name, .fee-tier--premium .fee-tier__name { margin-left: 0; }
  .fee-tier__level { font-family: "Montserrat", sans-serif; font-weight: 700; font-size: 12.5px; margin-left: 12px; line-height: 1.25; }
  .fee-tier--standard .fee-tier__level, .fee-tier--premium .fee-tier__level { margin-left: 6px; }
  .fee-tier__lead { margin-left: 6px; }
  .fee-tier ul { list-style: none; }
  .fee-tier--basic ul { margin-left: 2px; }
  .fee-tier li { position: relative; padding-left: 10px; }
  .fee-tier li::before { content: ""; position: absolute; left: 0; top: 7px; width: 4px; height: 4px; border-radius: 50%; background: var(--white); }
  .fee-tier--standard ul, .fee-tier--premium ul { margin-left: 4px; }
  .fee-tier__indent { padding-left: 8px; }
</style>
</head>
<body>

<section class="page page--intro">
  <div class="hero" role="img" aria-label="Photograph of a group of people silhouetted against a dusk sky"></div>
  <h1 class="hero__title">Meridian Foundation</h1>
  <p class="hero__subtitle">Fiscal Sponsorship Program</p>
  <p class="hero__intro"><strong>The Meridian Foundation, founded in 2010</strong>, exists to support social impact campaigns and organizations through educational, public engagement, and awareness efforts.<br>Its vision is to strengthen the capacity of the social impact sector and its leaders by providing top-tier fiscal sponsorship services.</p>
  <svg class="hero__notch" viewBox="0 0 566 30" preserveAspectRatio="none" aria-hidden="true">
    <polygon points="0,9 302,9 316,17 566,17 566,30 0,30" fill="#ffffff"/>
  </svg>

  <div class="definition">Fiscal sponsorship refers to the practice of non-profit organizations offering their legal and tax-exempt status to charitable projects or groups engaged in activities related to the sponsoring organization's mission. Fiscal sponsors provide oversight, financial management, and other administrative services to build the capacity of charitable projects.</div>
  <svg class="definition__bevel" viewBox="0 0 19 126" preserveAspectRatio="none" aria-hidden="true">
    <polygon points="0,0 19,9 19,117 0,126" fill="#0b2f66"/>
  </svg>
  <h2 class="definition__heading">WHAT IS<br>FISCAL<br>SPONSORSHIP?</h2>

  <div class="eligibility">
    <p class="eligibility__question">What kinds of projects are eligible for fiscal sponsorship?</p>
    <p class="eligibility__answer">Fiscal sponsorship refers to the practice of non-profit organizations offering their legal and tax-exempt status to charitable projects or groups engaged in activities related to the sponsoring organization's mission. Fiscal sponsors provide oversight, financial management, and other administrative services to build the capacity of charitable projects.</p>
  </div>

  <h2 class="philosophy__heading">FISCAL<br>SPONSORSHIP<br>PROGRAM<br>PHILOSOPHY</h2>
  <svg class="philosophy__bevel" viewBox="0 0 18 136" preserveAspectRatio="none" aria-hidden="true">
    <polygon points="0,0 18,0 18,136 0,136" fill="#0b2f66"/>
  </svg>
  <div class="philosophy__text">
    <p>We believe we can accelerate the pace and scale of social change by providing strategic back office support to emerging projects, leaders and ideas.</p>
    <p>By providing light touch administrative and capacity building services, our fiscal sponsorship program takes the administrative burden off the shoulders of leaders and their projects to allow them to focus on what they do best - achieving impact and changing the world.</p>
  </div>
</section>

<section class="page page--details">
  <h2 class="values__band">ORGANIZATIONAL VALUES</h2>
  <ul class="values__list">
    <li><span class="value__name">Trust:</span> We believe that all successful partnerships begin with a foundation of trust.</li>
    <li><span class="value__name">Relationships:</span> Our partners are central to our work. We honor our relationships through respect, communication and transparency.</li>
    <li><span class="value__name">Embrace Complexity and Risk:</span> We understand that bold solutions to intractable social issues often require both complexity and risk.</li>
    <li><span class="value__name">Innovation:</span> We embrace continuous improvement, bold creativity and change.</li>
    <li><span class="value__name">Diversity:</span> We believe that all voices matter and that effective solutions are created when decision-making is inclusive across social, cultural and economic backgrounds.</li>
  </ul>

  <h2 class="commitments__band">Meridian Foundation – Program Commitments</h2>
  <ul class="commitments__list">
    <li><svg viewBox="0 0 16 13" aria-hidden="true"><path d="M1 7 L6 11.5 L15 1.5" fill="none" stroke="#0a84ff" stroke-width="2.6" stroke-linecap="round" stroke-linejoin="round"/></svg>Fast, simple and efficient fiscal sponsorship program</li>
    <li><svg viewBox="0 0 16 13" aria-hidden="true"><path d="M1 7 L6 11.5 L15 1.5" fill="none" stroke="#0a84ff" stroke-width="2.6" stroke-linecap="round" stroke-linejoin="round"/></svg>Free and fast approval process - our application can be completed in 30 minutes or less. There is no fee to apply, and most projects can expect to receive a response on their application within 2 weeks</li>
    <li><svg viewBox="0 0 16 13" aria-hidden="true"><path d="M1 7 L6 11.5 L15 1.5" fill="none" stroke="#0a84ff" stroke-width="2.6" stroke-linecap="round" stroke-linejoin="round"/></svg>No fees and no minimums; projects of any size are welcome to apply</li>
    <li><svg viewBox="0 0 16 13" aria-hidden="true"><path d="M1 7 L6 11.5 L15 1.5" fill="none" stroke="#0a84ff" stroke-width="2.6" stroke-linecap="round" stroke-linejoin="round"/></svg>Easy onboarding process</li>
    <li><svg viewBox="0 0 16 13" aria-hidden="true"><path d="M1 7 L6 11.5 L15 1.5" fill="none" stroke="#0a84ff" stroke-width="2.6" stroke-linecap="round" stroke-linejoin="round"/></svg>Dedicated customer service and customization of services, tailored to the individual sponsored project's needs</li>
    <li><svg viewBox="0 0 16 13" aria-hidden="true"><path d="M1 7 L6 11.5 L15 1.5" fill="none" stroke="#0a84ff" stroke-width="2.6" stroke-linecap="round" stroke-linejoin="round"/></svg>Complex, hybrid structures, partnerships and coalitions are strongly encouraged to apply</li>
  </ul>

  <h2 class="fees__title">FEE STRUCTURE</h2>

  <div class="fee-tier fee-tier--basic">
    <h3 class="fee-tier__name">BASIC | FEE - 4%</h3>
    <p class="fee-tier__level">Limited</p>
    <ul>
      <li>Project Fund Set-Up</li>
      <li>Administration and Management</li>
      <li>Financial Management</li>
      <li>Grant Proposal Review</li>
      <li>Grant Contract Review</li>
      <li>Project Reporting</li>
      <li>Insurance</li>
      <li>Annual Audit and Form 990</li>
    </ul>
  </div>

  <div class="fee-tier fee-tier--standard">
    <h3 class="fee-tier__name">STANDARD | FEE - 6%</h3>
    <p class="fee-tier__level">Comprehensive</p>
    <p class="fee-tier__lead">Basic Services +</p>
    <ul>
      <li>Customized Financial Reporting</li>
      <li>Monthly Financial Statements</li>
      <li>Subgranting/regranting to<br>U.S.-based organizations</li>
      <li>Management of Vendor and<br>Independent Contractors (1099s)</li>
    </ul>
  </div>

  <div class="fee-tier fee-tier--premium">
    <h3 class="fee-tier__name">PREMIUM | FEE - 10% +</h3>
    <p class="fee-tier__level">Custom</p>
    <p class="fee-tier__lead">Standard Services + custom<br>services tailored to individual<br>project needs.<br>Customization Options:</p>
    <ul>
      <li>Subgranting/regranting to</li>
      <li>international organizations</li>
      <li>Lobbying Filings</li>
    </ul>
    <p class="fee-tier__lead fee-tier__indent">Project Audit</p>
    <ul>
      <li>Grant Writing Assistance</li>
    </ul>
    <p class="fee-tier__lead fee-tier__indent">One-on-One Coaching</p>
  </div>
</section>

</body>
</html>
```